Corvatel Website Graphic design

we want a replacement of existing designs in our existing website.. we want you to suggest and create a better graphical designs which suits our service with good representation explaining our process and services
Website Url: https://corvatelq.example
Basic Requirements -
1. Flat architecture
2. A good color palette
3. Icons to support the Content
4. Consistent Images in alignment with the Business
5. Use white space to let the Content breathe

Target Market(s)

Manufacturers & E-Commerce Distributors

Industry/Entity Type

Data Service

Colors

Designer to choose colors to be used in the design.

Requirements
Must have
• Creativity and originality
Nice to have
• Try to keep it Simple

```html
<!DOCTYPE html>
<html lang="en">
<head>
<meta charset="utf-8">
<title>Corvatel Solutions</title>
<link rel="stylesheet" href="https://fonts.googleapis.com/css2?family=Montserrat:wght@400;500;600;700&family=Questrial&display=swap">
<style>
:root{
  --blue:#4a86f0;
  --navy:#0c0c47;
  --ink:#111;
  --muted:#555;
  --line:#ececec;
  --white:#fff;
  --black:#000;
  --red:#e0392b;
}
*{margin:0;padding:0;box-sizing:border-box}
html,body{width:1200px;height:3750px;overflow:hidden;background:var(--white)}
body{position:relative;font-family:"Questrial",sans-serif;color:var(--ink)}
h1,h2,h3,p{font-weight:inherit}
.abs{position:absolute}
.nowrap{white-space:nowrap}

/* header */
.site-header{top:0;left:0;width:1200px;height:87px;background:var(--white)}
.brand{left:147px;top:22px;display:flex;align-items:center;gap:8px;font-size:21px;line-height:20px;color:var(--ink)}
.brand-dot{width:40px;height:40px;border-radius:50%;background:var(--blue)}
.main-nav{top:30px;left:0;font-size:15px;font-family:"Montserrat",sans-serif;font-weight:500}
.main-nav span{position:absolute;white-space:nowrap}
.main-nav .active{color:var(--blue)}

/* hero */
.hero{top:87px;left:0;width:1200px;height:464px;
  background:
    radial-gradient(ellipse 190px 140px at 29% 60%,rgba(230,30,45,.55),rgba(230,30,45,0) 100%),
    radial-gradient(ellipse 160px 70px at 28% 42%,rgba(245,245,245,.45),rgba(245,245,245,0) 100%),
    radial-gradient(ellipse 90px 80px at 20% 58%,rgba(40,140,60,.45),rgba(40,140,60,0) 100%),
    linear-gradient(180deg,#6f8798 0%,#4f6a7d 45%,#2c3f4e 75%,#1a2631 100%)}
.hero-title{left:537px;top:66px;width:230px;font-family:"Montserrat",sans-serif;font-weight:700;font-size:38px;line-height:45px;color:var(--white);letter-spacing:1.5px;text-align:center}
.hero-text{left:542px;top:190px;font-size:19.5px;line-height:22.5px;color:var(--white);letter-spacing:.3px}
.btn{position:absolute;height:31px;font-size:16px;line-height:31px;text-align:center}
.btn-light{left:542px;top:335px;width:135px;background:var(--white);color:var(--ink)}
.btn-blue{left:706px;top:335px;width:134px;background:var(--blue);color:var(--white)}

/* section titles */
.eyebrow{left:0;width:1200px;font-size:20px;text-align:center}
.section-title{left:0;width:1200px;font-family:"Montserrat",sans-serif;font-weight:700;font-size:23px;line-height:27px;text-align:center;letter-spacing:.5px}

/* cards */
.card{position:absolute;background:var(--white);border:1px solid var(--line);box-shadow:0 1px 4px rgba(0,0,0,.05);overflow:hidden}
.card-media{position:absolute;left:0;top:0;width:100%}
.svc-title{position:absolute;left:0;width:100%;font-family:"Montserrat",sans-serif;font-weight:700;font-size:15px;text-align:center;line-height:18px}
.svc-text{position:absolute;left:0;width:100%;font-size:12px;line-height:18.5px;color:var(--muted);text-align:center;white-space:nowrap}
.svc-link{position:absolute;left:0;width:100%;text-align:center;font-size:15px;font-weight:600;font-family:"Montserrat",sans-serif}
.dots{display:flex;gap:5px}
.dots i{width:9px;height:9px;border-radius:50%;background:#1f3a4a;display:block}
.dots i.on{background:#e23}

/* about */
.about{top:1110px;left:0;width:1200px;height:524px;
  background:
    radial-gradient(ellipse 420px 260px at 20% 15%,rgba(205,190,178,.55),rgba(205,190,178,0) 100%),
    radial-gradient(ellipse 300px 120px at 65% 55%,rgba(20,20,22,.55),rgba(20,20,22,0) 100%),
    linear-gradient(180deg,#8f8077 0%,#6c6058 35%,#4e4640 65%,#2e2925 100%)}
.about-title{left:0;width:1258px;top:46px;font-family:"Montserrat",sans-serif;font-weight:700;font-size:27px;color:var(--white);text-align:center}
.about-text{left:513px;top:86px;font-family:"Montserrat",sans-serif;font-size:18.5px;line-height:22.5px;color:var(--white);white-space:nowrap}
.about-link{left:962px;top:194px;font-size:15px;color:var(--white);font-weight:600;font-family:"Montserrat",sans-serif;border-bottom:2px solid var(--white);padding-bottom:4px}

/* blog */
.blog-title{position:absolute;left:0;width:100%;top:186px;font-family:"Montserrat",sans-serif;font-weight:700;font-size:11px;text-align:center;line-height:13px}
.blog-meta{position:absolute;left:3px;right:3px;top:213px;display:flex;justify-content:space-between;font-size:12px;color:var(--muted)}

/* solutions */
.sol-icon{position:absolute;width:38px;height:38px}
.sol-title{position:absolute;font-size:17px;line-height:18px;color:#222;font-weight:400;white-space:nowrap}
.sol-text{position:absolute;font-size:10.5px;line-height:15px;color:#444;white-space:nowrap}
.sol-link{position:absolute;font-size:10.5px;color:var(--blue)}

/* facts */
.facts{top:2698px;left:0;width:1200px;height:342px;background:var(--navy);color:var(--white)}
.fact{position:absolute;width:300px;text-align:center}
.fact-num{font-family:"Montserrat",sans-serif;font-size:24px;font-weight:500}
.fact-label{font-family:"Montserrat",sans-serif;font-size:16px;margin-top:10px}
.fact-text{font-size:10.5px;line-height:15px;margin-top:10px}
.facts .dots i{background:#5a7a8a}
.facts .dots i.on{background:var(--white)}

/* team */
.team-top{position:absolute;left:0;top:0;width:100%;height:145px;background:var(--blue);overflow:hidden}
.avatar{position:absolute;top:8px;left:50%;margin-left:-70px;width:140px;height:140px;border-radius:50%;
  background:radial-gradient(ellipse 70px 40px at 50% 100%,#2a2a33 0%,#2a2a33 60%,rgba(42,42,51,0) 100%),
             radial-gradient(ellipse 42px 50px at 50% 45%,#8a5a3c 0%,#7a4c30 70%,rgba(122,76,48,0) 100%),
             #f6f6f6}
.team-name{position:absolute;left:0;width:100%;top:173px;text-align:center;font-family:"Montserrat",sans-serif;font-weight:700;font-size:11px}
.team-role{position:absolute;left:0;width:100%;top:188px;text-align:center;font-size:12px;color:var(--muted)}
.socials{position:absolute;top:219px;left:0;width:100%;display:flex;justify-content:center;gap:17px}
.socials i{display:block;width:30px;height:30px;border-radius:50%;background:var(--blue)}
.socials i.red{background:var(--red)}

/* footer */
.site-footer{top:3495px;left:0;width:1200px;height:255px;background:var(--black);color:var(--white)}
.foot-head{position:absolute;top:25px;font-size:16px;color:#ddd}
.foot-links{position:absolute;font-family:"Montserrat",sans-serif;font-weight:700;line-height:45px}
.foot-contact{position:absolute;left:580px;width:190px;top:68px;text-align:center;font-size:16px;line-height:42px;color:#ddd}
.newsletter{position:absolute;left:835px;top:87px;width:214px;height:30px;display:flex}
.newsletter .field{flex:1;background:var(--white);color:#777;font-size:13px;padding:6px;border:1px solid #ccc}
.newsletter .send{width:48px;background:var(--blue);display:flex;align-items:center;justify-content:center}
</style>
</head>
<body>

<header class="abs site-header">
  <div class="abs brand"><span class="brand-dot"></span><span>Corvatel<br>Solutions</span></div>
  <nav class="abs main-nav">
    <span class="active" style="left:565px">Home</span>
    <span style="left:653px">About</span>
    <span style="left:747px">Services</span>
    <span style="left:861px">Solutions</span>
    <span style="left:981px">Contact</span>
  </nav>
</header>

<section class="abs hero" role="img" aria-label="Photograph of a colourful puzzle cube on a dark blue-grey surface">
  <h1 class="abs hero-title">Corvatel<br>Solutions</h1>
  <p class="abs hero-text nowrap">Get your large complexEnterprise data<br>transformed into value drivenstructured i<br>nformationto supercharge your business.</p>
  <div class="btn btn-light">About Us</div>
  <div class="btn btn-blue">Contact Now</div>
</section>

<p class="abs eyebrow" style="top:597px">Services We Provide</p>
<h2 class="abs section-title" style="top:640px">Why you need a data<br>management today.</h2>

<article class="card" style="left:147px;top:743px;width:289px;height:312px">
  <div class="card-media" style="height:166px;background:radial-gradient(ellipse 90px 60px at 40% 70%,#f3f5f7 0%,rgba(243,245,247,0) 100%),radial-gradient(ellipse 80px 50px at 70% 85%,#6a86ad 0%,rgba(106,134,173,0) 100%),linear-gradient(180deg,#bcd2e4 0%,#d9e3ea 40%,#a4b2bf 70%,#7890ac 100%)" role="img" aria-label="Photo of two people working with a laptop outdoors"></div>
  <h3 class="svc-title" style="top:180px">Master Data Management</h3>
  <p class="svc-text" style="top:203px">You can choose from 320+ icons and place it.<br>All icons are pixel-perfect, hand-crafted &amp;<br>perfectly scalable. Awesome, eh?</p>
  <span class="svc-link" style="top:274px">learn more</span>
</article>
<article class="card" style="left:454px;top:743px;width:292px;height:312px">
  <div class="card-media" style="height:166px;background:radial-gradient(ellipse 80px 45px at 45% 50%,#2f78d8 0%,rgba(47,120,216,0) 100%),radial-gradient(ellipse 70px 60px at 10% 5%,#4d6a2e 0%,rgba(77,106,46,0) 100%),linear-gradient(90deg,#0c1016 0%,#111a26 50%,#0c1016 88%,#f2dede 100%)" role="img" aria-label="Photo of a laptop showing sales charts"></div>
  <h3 class="svc-title" style="top:179px">E-Commerce Data<br>Management</h3>
  <p class="svc-text" style="top:215px">You can choose from 320+ icons and place it.<br>All icons are pixel-perfect, hand-crafted &amp;<br>perfectly scalable. Awesome, eh?</p>
  <span class="svc-link" style="top:273px">learn more</span>
</article>
<article class="card" style="left:760px;top:743px;width:291px;height:312px">
  <div class="card-media" style="height:166px;background:linear-gradient(180deg,#2f86b8 0%,#4a9cc4 12%,#a9b0ae 20%,#8c9190 50%,#6e7372 75%,#5d7a3a 88%,#3f6a2c 100%)" role="img" aria-label="Photo of a large dam wall"></div>
  <h3 class="svc-title" style="top:180px">Support Services</h3>
  <p class="svc-text" style="top:207px">You can choose from 320+ icons and place it.<br>All icons are pixel-perfect, hand-crafted &amp;<br>perfectly scalable. Awesome, eh?</p>
  <span class="svc-link" style="top:274px">learn more</span>
</article>
<div class="abs dots" style="left:565px;top:1079px"><i></i><i class="on"></i><i></i><i></i></div>

<section class="abs about" role="img" aria-label="Photo of an office desk with computers and a lamp">
  <h2 class="abs about-title">About Us</h2>
  <p class="abs about-text">Corvatel Solutions specializes in extracting business<br>centric information from large, complex and disparate<br>sources to realize full potential of Enterprise and<br>E-Commerce implementations.</p>
  <span class="abs about-link">learn more</span>
</section>

<p class="abs eyebrow" style="top:1688px">Daily Blogs</p>
<h2 class="abs section-title" style="top:1728px">Read all the stories<br>from journal</h2>

<article class="card" style="left:147px;top:1805px;width:213px;height:240px">
  <div class="card-media" style="height:168px;background:radial-gradient(ellipse 50px 25px at 35% 60%,#b82a2a 0%,rgba(184,42,42,0) 100%),linear-gradient(160deg,#f0f0f0 0%,#c9c9c9 45%,#7a7a7a 75%,#3e3e3e 100%)" role="img" aria-label="Photo of a hand holding a card near a laptop"></div>
  <h3 class="blog-title">10 Best Practices in E-commerce</h3>
  <div class="blog-meta"><span>Lena Marsh</span><span>April 15, 2019</span></div>
</article>
<article class="card" style="left:380px;top:1805px;width:212px;height:240px">
  <div class="card-media" style="height:168px;background:radial-gradient(ellipse 90px 50px at 50% 45%,#2d5590 0%,rgba(45,85,144,0) 100%),linear-gradient(160deg,#1c2d44 0%,#0c1726 55%,#304a72 100%)" role="img" aria-label="Photo of code on a laptop screen"></div>
  <h3 class="blog-title">Best Practices – Successful<br>Data Cleaning</h3>
  <div class="blog-meta"><span>Lena Marsh</span><span>April 15, 2019</span></div>
</article>
<article class="card" style="left:611px;top:1805px;width:210px;height:240px">
  <div class="card-media" style="height:168px;background:radial-gradient(ellipse 80px 40px at 45% 70%,#b89c7a 0%,rgba(184,156,122,0) 100%),linear-gradient(180deg,#dcdcdc 0%,#9a9a9a 40%,#5a5a5a 70%,#2e2e2e 100%)" role="img" aria-label="Photo of a team working at a shared table"></div>
  <h3 class="blog-title">Get Your Support</h3>
  <div class="blog-meta"><span>Lena Marsh</span><span>April 15, 2019</span></div>
</article>
<article class="card" style="left:836px;top:1805px;width:213px;height:240px">
  <div class="card-media" style="height:168px;background:radial-gradient(ellipse 70px 50px at 40% 70%,#f3f5f7 0%,rgba(243,245,247,0) 100%),radial-gradient(ellipse 70px 50px at 70% 85%,#6a86ad 0%,rgba(106,134,173,0) 100%),linear-gradient(180deg,#bcd2e4 0%,#d9e3ea 40%,#a4b2bf 70%,#7890ac 100%)" role="img" aria-label="Photo of two people working with a laptop outdoors"></div>
  <h3 class="blog-title">10 Best Practices in E-commerce</h3>
  <div class="blog-meta"><span>Lena Marsh</span><span>April 15, 2019</span></div>
</article>

<div class="abs" style="left:0;top:2123px;width:1200px;height:1px;background:var(--line)"></div>

<p class="abs eyebrow" style="top:2158px">Our Solution</p>
<h2 class="abs section-title" style="top:2198px">Solutions We Made</h2>

<svg width="0" height="0" style="position:absolute">
  <defs>
    <symbol id="ic-dollar" viewBox="0 0 38 38"><circle cx="19" cy="19" r="15" fill="none" stroke="#4a86f0" stroke-width="2"/><path d="M23 14c-1-1.5-7-2.5-7 1s7 2 7 6-6 3-8 1M19 10v18" fill="none" stroke="#4a86f0" stroke-width="2" stroke-linecap="round"/></symbol>
    <symbol id="ic-hands" viewBox="0 0 38 38"><path d="M3 12l8-3 8 5 8-5 8 3v10l-9 7-7-5-7 4-9-8z" fill="none" stroke="#4a86f0" stroke-width="2" stroke-linejoin="round"/></symbol>
    <symbol id="ic-box" viewBox="0 0 38 38"><path d="M19 5l14 7v14l-14 7-14-7V12z M5 12l14 7 14-7 M19 19v14" fill="none" stroke="#4a86f0" stroke-width="2" stroke-linejoin="round"/></symbol>
  </defs>
</svg>

<div class="card" style="left:147px;top:2305px;width:287px;height:153px">
  <svg class="sol-icon" style="left:6px;top:16px"><use href="#ic-dollar"/></svg>
  <h3 class="sol-title" style="left:75px;top:28px">Spend Analysis</h3>
  <p class="sol-text" style="left:77px;top:66px">With a flexible data model that can<br>processany kind of data to provide</p>
  <span class="sol-link" style="left:77px;top:112px">Read More</span>
</div>
<div class="card" style="left:454px;top:2305px;width:288px;height:153px">
  <svg class="sol-icon" style="left:13px;top:10px"><use href="#ic-hands"/></svg>
  <h3 class="sol-title" style="left:74px;top:28px;text-align:center">Vendor Relationship<br>Management</h3>
  <p class="sol-text" style="left:74px;top:72px">Gain better control over who buys wh<br>and when with less work on everyone.</p>
  <span class="sol-link" style="left:76px;top:116px">Read More</span>
</div>
<div class="card" style="left:762px;top:2305px;width:288px;height:153px">
  <svg class="sol-icon" style="left:14px;top:14px"><use href="#ic-box"/></svg>
  <h3 class="sol-title" style="left:76px;top:34px;text-align:center">Purchase Requisition<br>&amp; Ordering System</h3>
  <p class="sol-text" style="left:67px;top:80px;text-align:center">The Module can handle Floating reque<br>for quotation (RFQ) with a suitable cro</p>
  <span class="sol-link" style="left:77px;top:126px">Read More</span>
</div>

<div class="card" style="left:147px;top:2490px;width:287px;height:153px">
  <svg class="sol-icon" style="left:15px;top:26px"><use href="#ic-dollar"/></svg>
  <h3 class="sol-title" style="left:73px;top:36px;text-align:center">Floating RFQ's<br>Analysis And Ordering</h3>
  <p class="sol-text" style="left:72px;top:80px;text-align:center">The Module can handle Floating reque<br>for quotation (RFQ) with a suitable cro</p>
  <span class="sol-link" style="left:72px;top:122px">Read More</span>
</div>
<div class="card" style="left:454px;top:2490px;width:288px;height:153px">
  <svg class="sol-icon" style="left:16px;top:26px"><use href="#ic-dollar"/></svg>
  <h3 class="sol-title" style="left:71px;top:36px">Setup Payments</h3>
  <p class="sol-text" style="left:79px;top:80px">This Module is a simple and affordab<br>way to accept payments online offer</p>
  <span class="sol-link" style="left:79px;top:118px">Read More</span>
</div>
<div class="card" style="left:762px;top:2490px;width:288px;height:153px">
  <svg class="sol-icon" style="left:12px;top:26px"><use href="#ic-dollar"/></svg>
  <h3 class="sol-title" style="left:65px;top:39px">Inventory Management</h3>
  <p class="sol-text" style="left:65px;top:70px">This module keeps full track of inventor<br>rom purchase till sale. Generates invoic</p>
  <span class="sol-link" style="left:65px;top:114px">Read More</span>
</div>

<section class="abs facts">
  <p class="abs" style="left:0;width:1150px;top:22px;text-align:center;font-size:20px">Facts</p>
  <h2 class="abs" style="left:0;width:1150px;top:55px;text-align:center;font-family:'Montserrat',sans-serif;font-weight:700;font-size:23px">Some Fun Facts</h2>
  <div class="fact" style="left:128px;top:118px"><div class="fact-num">220</div><div class="fact-label">Career Opurtunities</div><div class="fact-text">With a flexible data model that can<br>processany kind of data to provide</div></div>
  <div class="fact" style="left:435px;top:118px"><div class="fact-num">40K</div><div class="fact-label">Income Statements</div><div class="fact-text">With a flexible data model that can<br>processany kind of data to provide</div><div style="font-size:10.5px;margin-top:12px;font-family:'Montserrat',sans-serif;font-weight:700">Read More</div></div>
  <div class="fact" style="left:752px;top:118px"><div class="fact-num">900</div><div class="fact-label">Credit s Earned</div><div class="fact-text">With a flexible data model that can<br>processany kind of data to provide</div></div>
  <div class="abs dots" style="left:557px;top:302px"><i></i><i class="on"></i><i></i><i></i></div>
</section>

<p class="abs eyebrow" style="top:3086px;width:1190px">Our Team</p>
<h2 class="abs section-title" style="top:3126px;width:1190px">Meet Our Team</h2>

<article class="card" style="left:147px;top:3195px;width:285px;height:260px">
  <div class="team-top"><div class="avatar" role="img" aria-label="Portrait photo of the president"></div></div>
  <h3 class="team-name">Rohan Veyra</h3><p class="team-role">President</p>
  <div class="socials"><i></i><i></i><i class="red"></i><i></i><i class="red"></i></div>
</article>
<article class="card" style="left:455px;top:3195px;width:285px;height:260px">
  <div class="team-top"><div class="avatar" role="img" aria-label="Portrait photo of the finance vice president"></div></div>
  <h3 class="team-name">Daniel Orsk</h3><p class="team-role">VP_Finance</p>
  <div class="socials"><i></i><i></i><i class="red"></i><i></i><i class="red"></i></div>
</article>
<article class="card" style="left:763px;top:3195px;width:285px;height:260px">
  <div class="team-top"><div class="avatar" role="img" aria-label="Portrait photo of the business development vice president"></div></div>
  <h3 class="team-name">Mira Talwen</h3><p class="team-role">VP - Business Development</p>
  <div class="socials"><i></i><i></i><i class="red"></i><i></i><i class="red"></i></div>
</article>

<footer class="abs site-footer">
  <span class="foot-head" style="left:143px">Ressource</span>
  <span class="foot-head" style="left:380px">Products</span>
  <span class="foot-head" style="left:608px">Contact Details</span>
  <span class="foot-head" style="left:834px">Sign up for newslettres</span>
  <div class="foot-links" style="left:148px;top:72px;font-size:22px">Home<br>About<br>Blog<br>Contact</div>
  <div class="foot-links" style="left:384px;top:74px;font-size:20px">Help<br>FAQ<br>Privacy Policy<br>Terms &amp; Condition</div>
  <div class="foot-contact">Contact Details<br>0 600 12 34 56<br>8:00 am 16:30 pm</div>
  <div class="newsletter">
    <div class="field">Enter Email Adress</div>
    <div class="send"><svg width="20" height="18" viewBox="0 0 20 18"><path d="M1 8L19 1 14 17 9 11z M9 11L19 1" fill="#fff" stroke="#fff" stroke-width="1" stroke-linejoin="round"/></svg></div>
  </div>
</footer>

</body>
</html>
```